Lost Teens Auto Doantion Website Design

Please create a new one page website design.

Current site: http://autosforyouth.net/

New WEBSITE address is: SedansForLostTeens.org

Use these sites for an idea of what I am looking for. I like these sites best: tiresforretirees.org and trucksforelders.org

Coding

Coded - Design and coding required

Number of Pages Required

1 page

```html
<!DOCTYPE html>
<html lang="en">
<head>
<meta charset="utf-8">
<title>Lost Teens Auto Doantion</title>
<link href="https://fonts.googleapis.com/css2?family=Poppins:wght@400;500;600;700&display=swap" rel="stylesheet">
<style>
:root{
  --blue:#3a8be0;
  --blue-dark:#2a76c9;
  --orange:#e4561d;
  --navy:#0c2a4c;
  --ink:#222;
  --muted:#666;
  --line:#d4d4d4;
  --grey-band:#f3f3f3;
  --pale-blue:#e2effb;
  --faq-grey:#8a8a8a;
}
*{box-sizing:border-box;margin:0;padding:0}
html,body{width:1200px;height:3913px;overflow:hidden}
body{font-family:"Poppins",sans-serif;color:var(--ink);background:#fff;position:relative}

/* header */
.site-header{position:absolute;left:0;top:0;width:1200px;height:78px;background:#fff}
.brand{position:absolute;left:86px;top:8px}
.brand-name{font-size:30px;font-weight:700;color:var(--blue);line-height:36px}
.brand-tag{font-size:14px;color:var(--blue);line-height:18px}
.main-nav{position:absolute;right:86px;top:28px;display:flex;gap:52px;font-size:15px;color:#444}

/* hero */
.hero-photo{position:absolute;left:0;top:78px;width:613px;height:538px;background:linear-gradient(160deg,#8bb2d6 0%,#9fb78a 45%,#4f6a35 100%)}
.hero-panel{position:absolute;left:613px;top:78px;width:587px;height:538px;background:linear-gradient(135deg,#4b9be8,#2f80d8);color:#fff}
.hero-panel h1{position:absolute;left:34px;top:28px;font-size:33px;font-weight:600;white-space:nowrap}
.pickup{position:absolute;left:34px;top:78px;font-size:23px;font-weight:500;white-space:nowrap}
.pickup b{margin-left:18px;font-weight:600}
.hero-rule{position:absolute;left:34px;right:0;height:1px;background:rgba(255,255,255,.5)}
.step-title{position:absolute;left:34px;top:150px;font-size:23px;white-space:nowrap}
.step-sub{position:absolute;left:34px;top:186px;font-size:17px;white-space:nowrap}
.boat{position:absolute;left:34px;top:230px;font-size:14px;display:flex;align-items:center;gap:14px}
.boat i{display:block;width:16px;height:16px;border:1px solid rgba(255,255,255,.7)}
.info{position:absolute;left:34px;top:268px;font-size:24px;font-weight:600}
.field{position:absolute;height:36px;border:1px solid rgba(255,255,255,.55);font-size:12px;color:rgba(255,255,255,.85);padding:0 10px;line-height:34px}
.field.sel::after{content:"";position:absolute;right:10px;top:13px;width:6px;height:6px;border-right:1.5px solid #fff;border-bottom:1.5px solid #fff;transform:rotate(45deg)}
.next-btn{position:absolute;height:36px;background:#fff;color:var(--blue);font-size:13px;font-weight:600;text-align:center;line-height:36px}

/* stats */
.stats-text{position:absolute;left:86px;top:668px;width:520px}
.stats-text .lead{font-size:18.5px;line-height:28px}
.stats-text .source{font-size:14px;line-height:22px;margin-top:18px}
.stat-box{position:absolute;width:238px;height:80px;background:var(--orange);color:#fff;text-align:center;padding-top:14px}
.stat-box b{display:block;font-size:19px;font-weight:600}
.stat-box span{font-size:18px}
.stats-photo{position:absolute;left:613px;top:616px;width:587px;height:391px;background:radial-gradient(circle at 55% 45%,#6a5a52,#2b2725 55%,#121212)}

/* about */
.about-band{position:absolute;left:0;top:1060px;width:1200px;height:177px;background:var(--pale-blue)}
.section-title{position:absolute;left:0;width:1200px;text-align:center;font-size:26px;font-weight:600;letter-spacing:.5px}
.video{position:absolute;left:261px;top:1158px;width:678px;height:397px;background:linear-gradient(135deg,#c9b46a,#e9d84c 40%,#6d7a88)}
.play{position:absolute;left:299px;top:158px}
.about-copy{position:absolute;left:86px;top:1592px;width:1028px;font-size:13.5px;line-height:23px;color:#555;text-align:center}
.donate-btn{position:absolute;left:514px;top:1741px;width:172px;height:48px;background:var(--orange);color:#fff;font-size:15px;font-weight:600;text-align:center;line-height:48px}

/* impact */
.impact{position:absolute;left:0;top:1842px;width:1200px;height:344px;background:linear-gradient(180deg,#1b1b1b,#2b2b2b 50%,#141414)}
.impact-box{position:absolute;top:52px;width:326px;height:162px;border:1px solid rgba(255,255,255,.35);color:#fff;text-align:center;padding-top:26px}
.impact-box b{display:block;font-size:34px;font-weight:600;margin-bottom:8px}
.impact-box span{display:block;font-size:17px;line-height:25px}
.impact-note{position:absolute;left:100px;top:240px;width:1000px;text-align:center;color:#fff;font-size:14px;line-height:26px}

/* missing kids */
.kid{position:absolute;top:2298px;width:149px}
.kid .photo{height:162px;background:linear-gradient(160deg,#d9b89a,#8a6a55)}
.kid p{font-size:12.5px;line-height:26px;color:#333;margin-top:12px}
.arrow{position:absolute;top:2368px}

/* contact */
.contact{position:absolute;left:0;top:2622px;width:1200px;height:352px;background:var(--grey-band)}
.input{position:absolute;height:42px;border:1px solid var(--line);background:#fff;font-size:12px;color:#999;padding:0 8px;line-height:40px}
.submit{position:absolute;left:543px;top:2902px;width:112px;height:40px;background:var(--blue);color:#fff;font-size:14px;font-weight:500;text-align:center;line-height:40px}

/* faq */
.faq-item{position:absolute;width:501px;height:46px;background:var(--faq-grey);color:#fff;font-size:15px;line-height:46px;padding-left:36px;white-space:nowrap}
.faq-item::before{content:"+";position:absolute;left:16px;font-size:18px;font-weight:600}
.faq-item.open{padding-left:60px}
.faq-item.open::before{left:0;width:44px;height:46px;background:var(--blue);text-align:center}
.faq-panel{position:absolute;left:86px;top:3164px;width:501px;height:252px;background:#f2f2f2;padding:18px 14px}
.faq-panel h3{font-size:18px;font-weight:500;margin-bottom:10px}
.faq-panel p{font-size:12.5px;line-height:20px;color:#666;margin-bottom:16px}

/* footer */
.site-footer{position:absolute;left:0;top:3705px;width:1200px;height:208px;background:var(--navy);color:#fff;text-align:center}
.site-footer h4{position:absolute;left:0;width:1200px;top:26px;font-size:17px;font-weight:600}
.legal{position:absolute;left:90px;width:1020px;top:68px;font-size:12.5px;line-height:24px}
.footer-rule{position:absolute;left:0;width:1200px;top:164px;height:1px;background:rgba(255,255,255,.2)}
.copyright{position:absolute;left:0;width:1200px;top:178px;font-size:12px;color:rgba(255,255,255,.75)}
</style>
</head>
<body>

<header class="site-header">
  <div class="brand">
    <div class="brand-name">Give Your Auto</div>
    <div class="brand-tag">Help Find Missing Kids</div>
  </div>
  <nav class="main-nav">
    <span>Home</span><span>About</span><span>Seek The Youth</span><span>Missing Kids</span><span>Contact</span><span>FAQ</span>
  </nav>
</header>

<section class="hero">
  <div class="hero-photo" role="img" aria-label="Empty swing on a playground"></div>
  <div class="hero-panel">
    <h1>Donate Your Car or Boat</h1>
    <div class="pickup">Fast Free Pickup <b>888-555-0142</b></div>
    <div class="hero-rule" style="top:136px"></div>
    <div class="step-title">2-Step Donation - Made Quick &amp; Easy</div>
    <div class="step-sub">Fill out the form &amp; help protect the future of children.</div>
    <div class="boat"><i></i>Donate a boat instead</div>
    <div class="info">Information</div>
    <div class="hero-rule" style="top:306px"></div>
    <div class="field" style="left:34px;top:332px;width:141px">Year</div>
    <div class="field" style="left:188px;top:332px;width:138px">Make</div>
    <div class="field" style="left:339px;top:332px;width:136px">Model</div>
    <div class="field sel" style="left:34px;top:389px;width:214px">Does it run?</div>
    <div class="field sel" style="left:264px;top:389px;width:211px">Do you have the title?</div>
    <div class="field sel" style="left:34px;top:446px;width:214px">Any major damage?</div>
    <div class="next-btn" style="left:264px;top:446px;width:211px">NEXT STEP</div>
  </div>
</section>

<section class="stats">
  <div class="stats-text">
    <p class="lead">Every 10 minutes, there's an attempt to abduct a child.<br>Most parents don't think it will happen to them.</p>
    <p class="source">According to the Department of Justice, each year,<br>there are approximately</p>
  </div>
  <div class="stat-box" style="left:86px;top:822px"><b>94,000</b><span>Missing Children</span></div>
  <div class="stat-box" style="left:350px;top:822px"><b>90,000</b><span>Runaways</span></div>
  <div class="stat-box" style="left:86px;top:925px"><b>300</b><span>Stranger Abductions</span></div>
  <div class="stat-box" style="left:350px;top:925px"><b>981</b><span>Family Abductions</span></div>
  <div class="stats-photo" role="img" aria-label="Frightened child with a hand covering the mouth"></div>
</section>

<section class="about">
  <div class="about-band"></div>
  <h2 class="section-title" style="top:1090px">ABOUT SEEK THE YOUTH</h2>
  <div class="video" role="img" aria-label="Video still of a child holding yellow balloons in a playground">
    <svg class="play" width="80" height="80" viewBox="0 0 80 80"><circle cx="40" cy="40" r="36" fill="none" stroke="#fff" stroke-width="6" opacity=".9"/><path d="M32 24 L56 40 L32 56Z" fill="#fff" opacity=".9"/></svg>
  </div>
  <p class="about-copy">Seek the Youth is a non-profit corporation dedicated to the recovery of missing children and to the prevention of the abuse and endangerment of children. Seek the Youth assists families searching for missing children by helping them to access local and federal law enforcement, advising them on the appropriate legal documents, and connecting them with other non-profit organizations or community resources that may help them in their search for their children. We educate parents and children on child safety, and work closely and in conjunction with the National Bureau for Lost and Vulnerable Youth. We have bilingual volunteers available to work with Spanish speaking families...</p>
  <div class="donate-btn">DONATE NOW &#9829;</div>
</section>

<section class="impact">
  <div class="impact-box" style="left:86px"><b>800,000</b><span>Children are reported missing<br>a year</span></div>
  <div class="impact-box" style="left:437px"><b>751,000</b><span>Children have seen the Seek the<br>Youth program</span></div>
  <div class="impact-box" style="left:788px"><b>400+</b><span>Open missing children<br>cases</span></div>
  <p class="impact-note">You can help protect the future of children by supporting Seek the Youth through your car donation. Your donated vehicle or vessel will be sold at auction and the net proceeds will be returned to Seek the Youth.</p>
</section>

<section class="missing">
  <h2 class="section-title" style="top:2236px">MISSING KIDS</h2>
  <svg class="arrow" style="left:48px" width="20" height="40" viewBox="0 0 20 40"><path d="M16 2 L4 20 L16 38" fill="none" stroke="#555" stroke-width="2"/></svg>
  <svg class="arrow" style="left:1132px" width="20" height="40" viewBox="0 0 20 40"><path d="M4 2 L16 20 L4 38" fill="none" stroke="#555" stroke-width="2"/></svg>
  <div class="kid" style="left:86px"><div class="photo" role="img" aria-label="Photo of a missing infant"></div><p>Jordan Ellison<br>City: Los Angeles<br>ABD: 10/19/2017<br>DOB: 9/14/2017</p></div>
  <div class="kid" style="left:261px"><div class="photo" role="img" aria-label="Photo of a missing toddler" style="background:linear-gradient(160deg,#b9a3c9,#6a4b6e)"></div><p>Jordan Ellison<br>City: Los Angeles<br>ABD: 10/19/2017<br>DOB: 9/14/2017</p></div>
  <div class="kid" style="left:436px"><div class="photo" role="img" aria-label="Photo of a missing boy" style="background:linear-gradient(160deg,#a88a6e,#4f3a2c)"></div><p>Jordan Ellison<br>City: Los Angeles<br>ABD: 10/19/2017<br>DOB: 9/14/2017</p></div>
  <div class="kid" style="left:613px"><div class="photo" role="img" aria-label="Photo of a missing baby girl" style="background:linear-gradient(160deg,#f1b3cf,#c0637f)"></div><p>Jordan Ellison<br>City: Los Angeles<br>ABD: 10/19/2017<br>DOB: 9/14/2017</p></div>
  <div class="kid" style="left:788px"><div class="photo" role="img" aria-label="Photo of a missing girl" style="background:linear-gradient(160deg,#e5866a,#8c4a3a)"></div><p>Jordan Ellison<br>City: Los Angeles<br>ABD: 10/19/2017<br>DOB: 9/14/2017</p></div>
  <div class="kid" style="left:965px"><div class="photo" role="img" aria-label="Photo of a missing young boy" style="background:linear-gradient(160deg,#d4a57f,#6c4a36)"></div><p>Jordan Ellison<br>City: Los Angeles<br>ABD: 10/19/2017<br>DOB: 9/14/2017</p></div>
</section>

<section class="contact">
  <h2 class="section-title" style="top:44px">CONTACT US</h2>
  <div class="input" style="left:86px;top:99px;width:235px">First Name</div>
  <div class="input" style="left:350px;top:99px;width:234px">Last Name</div>
  <div class="input" style="left:613px;top:99px;width:235px">Phone number</div>
  <div class="input" style="left:877px;top:99px;width:237px">Email address</div>
  <div class="input" style="left:86px;top:162px;width:1028px;height:89px">Your message</div>
</section>
<div class="submit">SUBMIT</div>

<section class="faq">
  <h2 class="section-title" style="top:3028px">FREQUENTLY ASKED QUESTIONS</h2>
  <div class="faq-item open" style="left:86px;top:3118px">Sed ut perspiciatis unde omnis iste natus error sit unde</div>
  <div class="faq-panel">
    <h3>Sed ut perspiciatis unde omnis iste natus error</h3>
    <p>Sed ut perspiciatis unde omnis iste natus error sit voluptatem accusantium doloremque laudantium, totam rem aperiam, eaque ipsa quae ab illo inventore veritatis et quasi architecto beatae vitae dicta sunt explicabo. Nemo enim ipsam voluptatem quia voluptas sit aspernatur aut odit aut fugit, sed quia consequuntur.</p>
    <p>Magni dolores eos qui ratione voluptatem sequi nesciunt. Neque porro quisquam est, qui dolorem ipsum quia dolor.</p>
  </div>
  <div class="faq-item" style="left:86px;top:3431px">Sed ut perspiciatis unde omnis iste natus error sit unde</div>
  <div class="faq-item" style="left:86px;top:3488px">Sed ut perspiciatis unde omnis iste natus error sit unde</div>
  <div class="faq-item" style="left:86px;top:3545px">Sed ut perspiciatis unde omnis iste natus error sit unde</div>
  <div class="faq-item" style="left:86px;top:3603px">Sed ut perspiciatis unde omnis iste natus error sit unde</div>
  <div class="faq-item" style="left:613px;top:3115px">Sed ut perspiciatis unde omnis iste natus error sit unde</div>
  <div class="faq-item" style="left:613px;top:3172px">Sed ut perspiciatis unde omnis iste natus error sit unde</div>
  <div class="faq-item" style="left:613px;top:3229px">Sed ut perspiciatis unde omnis iste natus error sit unde</div>
  <div class="faq-item" style="left:613px;top:3287px">Sed ut perspiciatis unde omnis iste natus error sit unde</div>
  <div class="faq-item" style="left:613px;top:3344px">Sed ut perspiciatis unde omnis iste natus error sit unde</div>
</section>

<footer class="site-footer">
  <h4>Privacy Policy</h4>
  <p class="legal">www.autosforyouth.net is not affiliated with Autos4Teens, AutosForTeens, WheelsForTeens, RidesaTeens, National ABLE! Rides For Teens, or any other website. Your donation to www.autosforyouth.net will benefit Seek The Youth, a registered Non Profit organization that helps find missing children. Seek The Youth is not affiliated with autos for teens, autosforteens, autos 4 teens, autos4teens, rides for teens, or rides 4 teens.</p>
  <div class="footer-rule"></div>
  <div class="copyright">&copy; Donate Autos for Youth 2018, All Rights Reserved</div>
</footer>

</body>
</html>
```